medical equipment home page redesign

We need a new home page for an existing store. We'll be redoing the entire site to make it more user friendly and follow talequill guidelines. We have a loose wireframe for the sections, but need help making it look great. The look should be clean, modern, professional, etc. We have a background image we would like to incorporate somewhere because we've just printed business cards and brochures that use this background image. We love parallax effects on backgrounds, so please allow extra big background images so we can utilize that effect. You can find images, etc from our site at brivolune.com. We like the way this site feels: http://tkro.palvenix.com/home/page/venue with the parallax background. And this one, too: https://www.muddersheriot.org/

Target Market(s)

people with chronic pain

Industry/Entity Type

Medical Equipment

Number of Pages Required

1 page

Font styles to use
Sans Serif

Colors
b8a6cd
6b449b
e4daeb

Requirements
Must have
• Please include sections from our wireframe. They don't have to look like the wireframe, but they do need to portray that information in each section.
Nice to have
• It would be great if you could include the background image we have attached
Should not have
• Should not look like the old site.

```html
<!DOCTYPE html>
<html lang="en">
<head>
<meta charset="utf-8">
<title>Brivolune – Light Therapy Home</title>
<link href="https://fonts.googleapis.com/css2?family=Lato:wght@300;400;700;900&family=Open+Sans:ital,wght@0,400;0,600;0,700;1,400&display=swap" rel="stylesheet">
<style>
:root{
  --ink:#2d2d3a;
  --muted:#7a7a86;
  --accent:#2fb8e6;
  --cta:#f0344f;
  --red:#ee3e4e;
  --green:#8ed156;
  --blue:#2fbde9;
  --lav:#b8a6cd;
  --plum:#6b449b;
  --mist:#e4daeb;
  --dark:#2a2a2f;
  --line:#e6e6ea;
}
*{box-sizing:border-box;margin:0;padding:0}
html,body{width:1200px;height:4120px;overflow:hidden}
body{font-family:"Open Sans",Arial,sans-serif;color:var(--ink);background:#fff;position:relative}
h1,h2,h3,h4{font-family:"Lato",Arial,sans-serif}
.section{position:absolute;left:0;width:1200px}
.btn{display:inline-block;font-family:"Lato",Arial,sans-serif;font-weight:700;font-size:13px;letter-spacing:1px;text-transform:uppercase;color:#fff;background:var(--cta);border-radius:4px;padding:12px 28px}
.btn--blue{background:var(--accent)}
.section-title{text-align:center;font-weight:400;font-size:34px;color:var(--ink)}
.section-title span{color:var(--accent)}

/* nav */
.site-nav{top:0;height:80px;background:#fff;display:flex;align-items:center;padding:0 60px;box-shadow:0 1px 4px rgba(0,0,0,.08);z-index:2}
.brand{display:flex;align-items:center;gap:8px;font-family:"Lato",sans-serif;font-weight:900;font-size:20px;color:var(--cta)}
.brand i{width:14px;height:14px;border-radius:50%;background:var(--cta);display:block}
.nav-links{display:flex;gap:36px;margin-left:110px;font-family:"Lato",sans-serif;font-size:12px;font-weight:700;letter-spacing:1px;text-transform:uppercase;color:var(--muted)}
.nav-links .current{color:var(--cta)}
.site-nav .btn{margin-left:50px;padding:10px 22px;font-size:11px}
.cart{margin-left:24px}

/* hero */
.hero{top:80px;height:400px;background:radial-gradient(circle at 12% 95%,#fff6d8 0,#ffc47a 10%,rgba(240,120,150,.6) 30%,transparent 55%),linear-gradient(180deg,#6d4fa0 0%,#b4609f 45%,#e58a8e 80%,#f2a582 100%);text-align:center;color:#fff}
.hero h1{font-size:52px;font-weight:700;line-height:1.15;padding-top:88px}
.hero p{font-size:22px;font-weight:700;font-family:"Lato",sans-serif;margin-top:10px}
.hero .btn{margin-top:36px;font-size:15px;padding:16px 34px}

/* features */
.features{top:480px;height:360px}
.features .section-title{margin-top:46px}
.feature-row{display:flex;justify-content:center;gap:32px;margin-top:50px}
.feature-card{width:266px;height:210px;background:#fff;box-shadow:0 2px 14px rgba(0,0,0,.08);text-align:center;padding:40px 30px}
.feature-card h3{font-size:15px;font-weight:400;margin-top:16px}
.feature-card p{font-size:11px;color:var(--muted);line-height:1.6;margin-top:8px}

/* how */
.how{top:860px;height:330px}
.how .section-title{margin-top:20px}
.how-row{display:flex;margin:40px auto 0;width:1010px;box-shadow:0 2px 14px rgba(0,0,0,.08)}
.how-card{flex:1;height:200px;padding:38px 28px;color:#fff}
.how-card h4{font-size:14px;font-weight:700;margin-top:12px}
.how-card p{font-size:11px;line-height:1.6;margin-top:8px}
.how-card--nir{background:#fff;color:var(--ink)}
.how-card--nir p{color:var(--muted)}
.how-card--red{background:var(--red)}
.how-card--green{background:var(--green)}
.how-card--blue{background:var(--blue)}

/* testimonials */
.testimonials{top:1290px;height:470px;background:linear-gradient(180deg,#6f6d66 0%,#8b8879 50%,#6b6e62 100%);color:#fff}
.testimonials h2{text-align:center;font-weight:400;font-size:32px;margin-top:44px}
.quote-row{display:flex;justify-content:center;gap:50px;margin-top:34px}
.quote{width:290px;font-size:12px;font-style:italic;line-height:1.7;text-align:center}
.quote strong{display:block;font-style:normal;margin-top:12px;font-size:12px}
.arrow{position:absolute;top:220px;font-size:28px;color:#fff}
.dots{position:absolute;bottom:40px;left:0;width:100%;display:flex;justify-content:center;gap:8px}
.dots i{width:8px;height:8px;border-radius:50%;background:rgba(255,255,255,.5);display:block}
.dots i:first-child{background:#fff}

/* pets */
.pets{top:1800px;height:420px}
.pets .section-title{margin-top:20px}
.pet-strip{display:flex;margin-top:34px;height:350px}
.pet-photo{flex:1}
.pet-photo--cat{background:linear-gradient(135deg,#e8566f,#f08b9a)}
.pet-photo--dog{background:linear-gradient(135deg,#4a6a3c,#a58355)}
.pet-photo--horse{background:linear-gradient(135deg,#8a8c95,#c9c6c0)}

/* products */
.products{top:2260px;height:540px;background:linear-gradient(180deg,#5c5c60,#8a8a8e)}
.products h2{text-align:center;color:#fff;font-weight:400;font-size:32px;margin-top:50px}
.product-row{display:flex;justify-content:center;gap:30px;margin-top:40px}
.product-card{width:224px;height:270px;background:#fff;text-align:center;padding:14px}
.product-photo{height:140px;background:linear-gradient(135deg,#2b2b30,#6a6a72)}
.product-card p{font-size:12px;margin-top:14px;line-height:1.5}
.product-card .btn{margin-top:14px;padding:8px 18px;font-size:10px}
.products .arrow{top:300px}
.browse-all{text-align:center;margin-top:40px}
.browse-all span{display:inline-block;border:1px solid #fff;color:#fff;font-family:"Lato",sans-serif;font-size:11px;font-weight:700;letter-spacing:1px;padding:10px 26px}

/* video */
.video{top:2800px;height:500px}
.video .section-title{margin-top:60px}
.video-frame{width:880px;height:340px;margin:30px auto 0;background:linear-gradient(135deg,#7a5a4a,#c5a36b 45%,#6f84a6);position:relative}
.play{position:absolute;left:50%;top:50%;transform:translate(-50%,-50%)}

/* blog */
.blog{top:3300px;height:480px}
.blog .section-title{margin-top:20px}
.blog-row{display:flex;justify-content:center;gap:40px;margin-top:36px}
.post{width:280px;text-align:center}
.post-photo{height:170px}
.post-photo--tie{background:linear-gradient(135deg,#6c2a22,#c9b5a0)}
.post-photo--soft{background:linear-gradient(135deg,#d9dde4,#8a9bb2)}
.post-photo--dose{background:linear-gradient(135deg,#1c1c22,#c83a4a 60%,#3a9b5a)}
.post h4{font-size:12px;font-weight:900;margin-top:14px}
.post .tinted{color:var(--cta)}
.post time{display:block;font-size:10px;color:var(--muted);margin-top:4px}
.post p{font-size:11px;color:var(--muted);line-height:1.6;margin-top:8px}
.blog .btn{display:block;width:140px;margin:34px auto 0;text-align:center;padding:12px 0}

/* newsletter */
.newsletter{top:3800px;height:260px;background:linear-gradient(180deg,#7a7d84,#5d6068);text-align:center;color:#fff}
.newsletter h2{font-weight:400;font-size:30px;margin-top:64px}
.newsletter p{font-size:12px;margin-top:8px}
.signup{display:flex;justify-content:center;margin-top:26px}
.signup span{width:300px;height:40px;border-bottom:1px solid #fff;text-align:left;font-size:12px;padding:12px 4px;color:rgba(255,255,255,.8)}
.signup .btn{border-radius:0;padding:12px 30px}
.site-footer{top:4060px;height:60px;background:var(--dark);color:#bbb;text-align:center;font-size:11px;letter-spacing:1px;line-height:60px}
</style>
</head>
<body>

<header class="section site-nav">
  <div class="brand"><i></i>Brivolune</div>
  <nav class="nav-links">
    <span>Home</span><span class="current">What's New</span><span>Learn More</span><span>Photo Gallery</span>
  </nav>
  <span class="btn">Shop Now</span>
  <svg class="cart" width="18" height="18" viewBox="0 0 24 24" fill="none" stroke="#555" stroke-width="2"><path d="M3 4h3l2 11h11l2-8H7"/><circle cx="10" cy="20" r="1.5"/><circle cx="18" cy="20" r="1.5"/></svg>
</header>

<section class="section hero" role="img" aria-label="Sunlight glowing through a purple and pink sky">
  <h1>Relieve the Pain and<br>Accelerate the Healing</h1>
  <p>Everyone deserves access to the pain free life</p>
  <span class="btn">Browse Now</span>
</section>

<section class="section features">
  <h2 class="section-title">We provide <span>quality products.</span></h2>
  <div class="feature-row">
    <div class="feature-card">
      <svg width="40" height="40" viewBox="0 0 40 40" fill="none" stroke="var(--cta)" stroke-width="2"><rect x="8" y="14" width="24" height="12" rx="6"/><line x1="20" y1="14" x2="20" y2="26"/><line x1="6" y1="34" x2="34" y2="6"/></svg>
      <h3>Drugs Free</h3>
      <p>Gentle light energy that supports the body's own healing without any medication.</p>
    </div>
    <div class="feature-card">
      <svg width="40" height="40" viewBox="0 0 40 40" fill="none" stroke="var(--cta)" stroke-width="2"><path d="M20 4l13 5v10c0 9-6 14-13 17C13 33 7 28 7 19V9z"/><path d="M14 20l4 4 8-8"/></svg>
      <h3>Safe</h3>
      <p>Non-invasive devices designed for simple and safe use at home every day.</p>
    </div>
    <div class="feature-card">
      <svg width="40" height="40" viewBox="0 0 40 40" fill="none" stroke="var(--cta)" stroke-width="2"><path d="M20 34S6 25 6 15a7 7 0 0 1 14-2 7 7 0 0 1 14 2c0 10-14 19-14 19z"/></svg>
      <h3>Pain Relief</h3>
      <p>Proven to ease sore muscles and stiff joints so you can move freely again.</p>
    </div>
  </div>
</section>

<section class="section how">
  <h2 class="section-title">How light therapy can <span>stop your pain?</span></h2>
  <div class="how-row">
    <div class="how-card how-card--nir">
      <svg width="30" height="30" viewBox="0 0 30 30" fill="none" stroke="#555" stroke-width="2"><path d="M6 4v8a6 6 0 0 0 12 0V4"/><path d="M12 18v4a5 5 0 0 0 10 0v-4"/><circle cx="22" cy="15" r="3"/></svg>
      <h4>NIR</h4><p>Near infrared light reaches deep tissue to support repair and reduce inflammation.</p>
    </div>
    <div class="how-card how-card--red">
      <svg width="30" height="30" viewBox="0 0 30 30" fill="none" stroke="#fff" stroke-width="2"><rect x="4" y="10" width="22" height="10" rx="5"/><line x1="15" y1="10" x2="15" y2="20"/></svg>
      <h4>Red</h4><p>Red light boosts cell energy and circulation for faster skin healing.</p>
    </div>
    <div class="how-card how-card--green">
      <svg width="30" height="30" viewBox="0 0 30 30" fill="none" stroke="#fff" stroke-width="2"><rect x="4" y="10" width="22" height="10" rx="5"/><line x1="15" y1="10" x2="15" y2="20"/></svg>
      <h4>Green</h4><p>Green light calms the nerves and helps balance the body's response.</p>
    </div>
    <div class="how-card how-card--blue">
      <svg width="30" height="30" viewBox="0 0 30 30" fill="none" stroke="#fff" stroke-width="2"><path d="M8 4h14l-3 10h6L11 27l3-10H8z"/></svg>
      <h4>Blue</h4><p>Blue light has a soothing effect and is known to support clear healthy skin.</p>
    </div>
  </div>
</section>

<section class="section testimonials" role="img" aria-label="Soft focus field of flowers behind the testimonials">
  <h2>Testimonials</h2>
  <span class="arrow" style="left:60px">&#8249;</span>
  <span class="arrow" style="right:60px">&#8250;</span>
  <div class="quote-row">
    <p class="quote">"My back had hurt for years and nothing seemed to help for long. After a few weeks with the lights I am sleeping through the night and walking again without pain. I tell everyone I know about it."<strong>Marla Quenby</strong></p>
    <p class="quote">"Fantastic treatment system. We use it every day on our dogs and on ourselves. Easy to use, well made and the results have been better than we hoped. Customer support answered every question quickly."<strong>Terrence Halvik, Owner</strong></p>
    <p class="quote">"The horse was lame and the vet offered little hope. We started daily sessions with the pads and within a month he was sound and back to work. A simple tool that made a real difference for us."<strong>Jane Orvell, Trainer</strong></p>
  </div>
  <div class="dots"><i></i><i></i><i></i></div>
</section>

<section class="section pets">
  <h2 class="section-title">Light Therapy <span>for your pets.</span></h2>
  <div class="pet-strip">
    <div class="pet-photo pet-photo--cat" role="img" aria-label="Kitten under pink light"></div>
    <div class="pet-photo pet-photo--dog" role="img" aria-label="Dog resting in a garden"></div>
    <div class="pet-photo pet-photo--horse" role="img" aria-label="Horse close-up"></div>
  </div>
</section>

<section class="section products" role="region" aria-label="Featured products">
  <h2>Featured Products.</h2>
  <span class="arrow" style="left:60px">&#8249;</span>
  <span class="arrow" style="right:60px">&#8250;</span>
  <div class="product-row">
    <div class="product-card"><div class="product-photo" role="img" aria-label="Handheld light device"></div><p>Complete Package<br>(Massage, Horse, Dog)</p><span class="btn">Add to cart</span></div>
    <div class="product-card"><div class="product-photo" role="img" aria-label="Handheld light device"></div><p>Complete Package<br>(Massage, Horse, Dog)</p><span class="btn">Add to cart</span></div>
    <div class="product-card"><div class="product-photo" role="img" aria-label="Handheld light device"></div><p>Complete Package<br>(Massage, Horse, Dog)</p><span class="btn">Add to cart</span></div>
    <div class="product-card"><div class="product-photo" role="img" aria-label="Handheld light device"></div><p>Complete Package<br>(Massage, Horse, Dog)</p><span class="btn">Add to cart</span></div>
  </div>
  <div class="browse-all"><span>Browse All</span></div>
</section>

<section class="section video">
  <h2 class="section-title">A very informative video <span>about the lights.</span></h2>
  <div class="video-frame" role="img" aria-label="Video still of two practitioners in a stable">
    <svg class="play" width="80" height="56" viewBox="0 0 80 56"><rect width="80" height="56" rx="12" fill="#e22"/><path d="M32 16l20 12-20 12z" fill="#fff"/></svg>
  </div>
</section>

<section class="section blog">
  <h2 class="section-title">From <span>Our Blog.</span></h2>
  <div class="blog-row">
    <article class="post"><div class="post-photo post-photo--tie" role="img" aria-label="Horse tied in a stable"></div><h4>BEST PRACTICES – DON'T CROSS-TIE!</h4><time>Jan 28, 2020</time><p>When we show people how to use their lights on horses, we stress how to position them safely.</p></article>
    <article class="post"><div class="post-photo post-photo--soft" role="img" aria-label="Reference software screen"></div><h4 class="tinted">POINTS PC SOFTWARE OR BACK HORSE'S QUARTERS LIGHT?</h4><time>Jan 28, 2020</time><p>When we show people how to use their lights on horses, we point them to the guide.</p></article>
    <article class="post"><div class="post-photo post-photo--dose" role="img" aria-label="Glowing light pads"></div><h4>LIGHT DOSING</h4><time>Jan 28, 2020</time><p>Please use the following chart to determine the amount of energy for each session.</p></article>
  </div>
  <span class="btn btn--blue">View All</span>
</section>

<section class="section newsletter" role="region" aria-label="Newsletter">
  <h2>Newsletter</h2>
  <p>Join our newsletter to get new exciting information</p>
  <div class="signup"><span>Your email address</span><span class="btn btn--blue">Submit</span></div>
</section>

<footer class="section site-footer">COPYRIGHT 2020. ALL RIGHTS RESERVED.</footer>

</body>
</html>
```